Veltrane New Business Card Design IT Company

PLEASE CHECK ATTACHED PDF DOC FOR DETAILS. I have put exactly what I want to save time and finish the project asap thanks.

Veltrane Consulting is an Information Management Consulting company providing IT Professional Services Consulting services to both Public and private sector.
Need a Business Card Design to represent. It has to be Premium Raised Spot Glass finish.
Company Name: Veltrane Consulting
Company Website: veltrane-example.com.au
Company Slogan: High Performance Meets Excellence
Name on Card: Tom Risley
Title: Managing Partner
Email: Tom.Risley@veltrane-example.com.au
Phone: 0472836105

Company Logo is under construction from PixelGuild
Company Logo & Company Name Font Color should Match and have to Electric Aqua Blue
Company Logo at the Back Side of the Card
Card Background color preference: Slight Grey or Black to make the logo and company Name stand Out.

Any Questions please Ask.

Industry/Entity Type

Construction

Contact Information for Business Card

PLEASE CHECK ATTACHED PDF DOC FOR DETAILS. I have put exactly what I want to save time and finish the project asap thanks
Name on Card: Tom Risley
Title: Managing Partner
Phone: 0472836105

Requirements
Must have
• PLEASE CHECK ATTACHED PDF DOC FOR DETAILS. I have put exactly what I want to save time and finish the project asap thanks
• Company Logo, Company Name, Company website Company Slogan at the back side of the Card with custom dark blue front and back background
• Company Logo, Company Name , Company Website at the Front of the Card Title and Name email and phone in the front also in white color font
Should not have
• Should not Have Decorative or Script Fonts
• Its a IT company so must be professional no flowers or waterfalls etc

```html
<!DOCTYPE html>
<html lang="en">
<head>
<meta charset="utf-8">
<title>Veltrane Consulting – Business Card</title>
<link rel="stylesheet" href="https://fonts.googleapis.com/css2?family=Questrial&family=Montserrat:wght@600;700&display=swap">
<style>
  :root {
    --page: #ffffff;
    --card-dark: #0c111a;
    --card-slate: #6a8593;
    --aqua: #3fb0e6;
    --aqua-light: #bff3fb;
    --slogan: #2fd3ee;
    --white-text: #f2f6f9;
  }
  * { margin: 0; padding: 0; box-sizing: border-box; }
  html, body {
    width: 923px; height: 1200px; overflow: hidden;
    background: var(--page);
  }
  .canvas { position: relative; width: 923px; height: 1200px; }

  .card {
    position: absolute; left: 43px; width: 843px; height: 520px;
    overflow: hidden;
  }
  .card--front { top: 55px; background: var(--card-dark); }
  .card--back  { top: 633px; background: var(--card-slate); }

  .brand-mark {
    position: absolute; right: 58px; top: 82px;
    display: flex; align-items: center; gap: 10px;
    font-family: "Questrial", sans-serif; font-size: 30px; line-height: 34px;
    color: var(--aqua);
  }
  .brand-mark__dot {
    width: 30px; height: 30px; border-radius: 50%;
    background: var(--aqua);
  }

  .company-name {
    position: absolute; left: 0; right: 0; top: 252px;
    text-align: center;
    font-family: "Montserrat", sans-serif; font-size: 50px; font-weight: 700;
    line-height: 60px;
    color: var(--aqua-light);
  }
  .slogan {
    position: absolute; left: 0; right: 0; top: 330px;
    text-align: center;
    font-family: "Questrial", sans-serif; font-size: 26px; line-height: 32px;
    color: var(--slogan);
  }
  .website {
    position: absolute; left: 0; right: 0; top: 468px;
    text-align: center;
    font-family: "Questrial", sans-serif; font-size: 25px; line-height: 30px;
    color: var(--white-text);
  }

  .person-name {
    position: absolute; left: 0; right: 0; top: 232px;
    text-align: center;
    font-family: "Montserrat", sans-serif; font-size: 40px; font-weight: 600;
    line-height: 50px;
    color: var(--white-text);
  }
  .person-title {
    position: absolute; left: 0; right: 0; top: 286px;
    text-align: center;
    font-family: "Questrial", sans-serif; font-size: 24px; line-height: 30px;
    color: var(--white-text);
  }
  .contact {
    position: absolute; left: 54px; top: 385px;
    list-style: none;
    font-family: "Questrial", sans-serif; font-size: 24px; line-height: 31px;
    color: var(--white-text);
  }
</style>
</head>
<body>
<main class="canvas">
  <section class="card card--front" aria-label="Card back side">
    <div class="brand-mark"><span class="brand-mark__dot"></span>Veltrane</div>
    <h1 class="company-name">Veltrane Consulting</h1>
    <p class="slogan">high performance meets excellence</p>
    <p class="website">veltrane-example.com.au</p>
  </section>

  <section class="card card--back" aria-label="Card front side">
    <div class="brand-mark"><span class="brand-mark__dot"></span>Veltrane</div>
    <h2 class="person-name">Tom Risley</h2>
    <p class="person-title">Managing Partner</p>
    <ul class="contact">
      <li>Phone: 047 283 6105</li>
      <li>Email: Tom.Risley@veltrane-example.com.au</li>
      <li>Web: veltrane-example.com.au</li>
    </ul>
  </section>
</main>
</body>
</html>
```